Antigen Preservation Bureau

The company will provide a contract research services to stabilize various viruses, viral vectors, and vaccines. It may offer some licensing opportunities for stabilizing technologies. Main area of applications are pharmaceutical, therapeutic, and vaccination field. The company aspires to develop room temperature vaccines for global distribution beyond the current cold chain.

Target Market(s)

pharmaceutical, therapeutic and vaccination fields

Coding

Coded - Design and coding required

Number of Pages Required

4 page

Requirements
Must have
• Incorporate a APB logo, attached at the bottom, on the Web page

```html
<!DOCTYPE html>
<html lang="en">
<head>
<meta charset="utf-8">
<title>Antigen Preservation Bureau</title>
<link href="https://fonts.googleapis.com/css2?family=Open+Sans:ital,wght@0,400;0,600;0,700;1,400&family=Montserrat:wght@600;700&display=swap" rel="stylesheet">
<style>
:root{
  --gold:#c9993f;
  --teal:#5b9f87;
  --teal-soft:#8ec4b0;
  --grey-box:#8a8a8a;
  --topbar:#4d4d4d;
  --ink:#1e1e1e;
  --text:#555;
  --muted:#888;
  --link:#2a6fa8;
  --light:#f4f4f4;
  --footer:#393939;
  --footer-bottom:#2e2e2e;
  --white:#fff;
}
*{margin:0;padding:0;box-sizing:border-box}
html,body{width:1200px;height:3734px;overflow:hidden}
body{position:relative;font-family:"Open Sans",Arial,sans-serif;color:var(--text);background:var(--white)}
.abs{position:absolute}

/* top bar */
.topbar{left:0;top:0;width:1200px;height:45px;background:var(--topbar);color:#ddd;font-size:12px}
.topbar .contact{left:95px;top:0;line-height:45px;display:flex;gap:22px}
.topbar .contact span{padding-left:22px;border-left:1px solid #777}
.topbar .contact span:last-child{border-right:1px solid #777;padding-right:22px}
.topbar .follow{left:765px;line-height:45px;display:flex;align-items:center;gap:12px}
.topbar .dot{width:12px;height:12px;border-radius:50%;background:#ddd;display:inline-block}
.topbar .cta{left:960px;top:0;width:140px;height:45px;background:#6a6a6a;color:#fff;font-weight:700;font-size:12px;text-align:center;line-height:45px}

/* nav */
.nav{left:0;top:45px;width:1200px;height:75px;background:var(--white)}
.brand{left:95px;top:12px;display:flex;align-items:center;gap:10px}
.brand .mark{width:44px;height:44px;border-radius:50%;background:var(--teal)}
.brand .name{font-size:14px;font-weight:700;color:var(--teal);line-height:16px;letter-spacing:1px;text-transform:uppercase}
.menu{top:0;line-height:75px;font-size:12px;font-weight:600;color:var(--ink)}

/* hero */
.hero{left:0;top:120px;width:1200px;height:617px;background:linear-gradient(100deg,#cfd5d8 0%,#9aa3a8 35%,#7d868b 60%,#5f676b 100%)}
.hero-copy{right:97px;top:130px;text-align:left;color:#fff}
.hero-copy h1{font-size:44px;font-weight:600;line-height:58px}
.hero-copy p{font-size:20px;font-weight:600;line-height:34px;text-align:right;margin-top:10px}
.btn-ghost{right:102px;top:408px;width:154px;height:45px;border:2px solid #fff;color:#fff;font-size:12px;font-weight:700;text-align:center;line-height:41px}

.badge{left:563px;top:700px;width:75px;height:75px;border-radius:50%;background:#fff;box-shadow:0 2px 8px rgba(0,0,0,.15);display:flex;align-items:center;justify-content:center}
.badge i{width:38px;height:38px;border-radius:50%;background:var(--teal);display:block}

.kicker{font-size:14px;color:var(--text);width:1200px;text-align:center}
.section-title{font-size:32px;font-weight:700;color:var(--ink);width:1200px;text-align:center}

/* offers */
.band{left:0;top:1203px;width:1200px;height:505px;background:linear-gradient(90deg,#7fb9a4,#6aa893 50%,#8bbfae)}
.card{top:951px;width:334px;height:426px;background:#fff;box-shadow:0 4px 14px rgba(0,0,0,.12)}
.card .photo{height:252px}
.card h3{font-size:18px;font-weight:700;color:var(--ink);margin:26px 40px 12px}
.card p{font-size:13px;line-height:21px;margin:0 40px}
.card .more{display:block;font-size:12px;font-weight:700;color:var(--link);margin:12px 40px 0}
.about{left:0;top:1455px;width:1200px;text-align:center;color:#fff}
.about h2{font-size:28px;font-weight:400;line-height:36px}
.about h2 b{font-weight:700;font-size:30px}
.about p{width:760px;margin:20px auto 0;font-size:13px;line-height:22px;color:#eef}

/* applications */
.app{top:1897px;width:313px;height:160px;color:#fff;text-align:center}
.app svg{margin-top:22px}
.app h4{font-family:"Montserrat",Arial,sans-serif;font-size:26px;font-weight:700;letter-spacing:.5px;margin-top:4px}
.app span{font-size:12px;font-weight:700}

/* news & reviews */
.light{left:0;top:2161px;width:1200px;height:553px;background:var(--light)}
.col-kicker{font-size:14px;color:var(--text)}
.col-title{font-size:32px;font-weight:700;color:var(--ink)}
.article{left:95px;width:470px;display:flex;gap:23px}
.article .thumb{width:124px;height:87px;flex:none}
.article time{font-size:12px;color:#7ac6d6;display:block;margin-top:8px}
.article p{font-size:13px;line-height:22px;color:#444;margin-top:24px}
.review{left:612px;top:2323px;width:488px;height:292px;background:#fff;box-shadow:0 2px 10px rgba(0,0,0,.08);padding:32px 40px}
.review blockquote{font-style:italic;font-size:14px;line-height:24px;color:#444}
.review h5{font-size:15px;font-weight:600;color:var(--ink);margin-top:22px}
.review small{font-size:12px;color:var(--muted)}
.arrow{top:2538px;width:44px;height:44px;border-radius:50%;display:flex;align-items:center;justify-content:center}

/* map & contact */
.map{left:0;top:2714px;width:1200px;height:443px;background:linear-gradient(135deg,#e6e6e6,#d8d8d8 50%,#e8e8e8)}
.contact-box{left:100px;top:2794px;width:338px;height:289px;background:var(--gold);color:#fff;padding:40px 46px;box-shadow:0 4px 16px rgba(0,0,0,.2)}
.contact-box h3{font-size:20px;font-weight:600;margin-bottom:26px}
.contact-box li{list-style:none;display:flex;gap:16px;font-size:14px;line-height:22px;margin-bottom:18px}
.contact-box svg{flex:none;margin-top:3px}
.stripe{left:0;top:3157px;width:1200px;height:20px;background:var(--teal)}

/* footer */
.footer{left:0;top:3177px;width:1200px;height:439px;background:var(--footer);color:#ccc}
.f-head{font-size:14px;font-weight:700;color:#fff;letter-spacing:1px}
.f-text{font-size:12px;line-height:22px;color:#ddd}
.tweet{display:flex;gap:14px;margin-bottom:22px}
.tweet i{width:8px;height:8px;margin-top:7px;border-radius:50%;background:#777;flex:none}
.links{font-size:12px;line-height:32px;color:#ccc;list-style:none}
.insta{width:67px;height:69px;background:#6d6d6d}
.subscribe{left:87px;top:3466px;width:237px;height:34px;border-radius:17px;background:#2d2d2d;font-size:12px;color:#777;line-height:34px;padding-left:16px}
.subscribe b{position:absolute;right:-8px;top:-2px;width:38px;height:38px;border-radius:50%;background:var(--gold);display:flex;align-items:center;justify-content:center}
.bottom{left:0;top:3616px;width:1200px;height:118px;background:var(--footer-bottom)}
.bottom .socials{left:87px;top:50px;display:flex;gap:24px}
.bottom .socials i{width:12px;height:12px;border-radius:50%;background:#ccc;display:block}
.bottom .copy{right:100px;top:46px;font-size:11px;color:#999}
</style>
</head>
<body>

<!-- top bar -->
<div class="abs topbar">
  <div class="abs contact"><span>Phone: (925) 555 0148</span><span>support@apb-lab.example</span></div>
  <div class="abs follow">Follow Us: <i class="dot"></i><i class="dot"></i><i class="dot"></i></div>
  <div class="abs cta">CONTACT US NOW</div>
</div>

<!-- navigation -->
<header class="abs nav">
  <div class="abs brand"><span class="mark"></span><span class="name">Antigen<br>Preservation<br>Bureau</span></div>
  <span class="abs menu" style="left:433px">HOME</span>
  <span class="abs menu" style="left:528px">ABOUT US</span>
  <span class="abs menu" style="left:622px">OUR SERVICES</span>
  <span class="abs menu" style="left:750px">NEWS &amp; EVENTS</span>
  <span class="abs menu" style="left:880px">PARTNERS</span>
  <span class="abs menu" style="left:977px">CONTACT</span>
  <svg class="abs" style="left:1083px;top:29px" width="17" height="17" viewBox="0 0 17 17"><circle cx="7" cy="7" r="5.5" fill="none" stroke="#222" stroke-width="2.2"/><line x1="11" y1="11" x2="16" y2="16" stroke="#222" stroke-width="2.4"/></svg>
</header>

<!-- hero -->
<section class="abs hero" role="img" aria-label="Scientist in a mask working at a microscope in a laboratory"></section>
<div class="abs hero-copy">
  <h1>Ask us How we can help</h1>
  <p>We have the facilities and expert knowledge to<br>meet your research needs.</p>
</div>
<div class="abs btn-ghost">LEARN MORE</div>
<div class="abs badge"><i></i></div>

<!-- offers -->
<div class="abs kicker" style="left:0;top:812px">For Better Welness &amp; Hope</div>
<h2 class="abs section-title" style="left:0;top:852px">What We Offers</h2>
<section class="abs band" role="img" aria-label="Teal-tinted photo of a researcher at a microscope"></section>

<article class="abs card" style="left:102px">
  <div class="photo" role="img" aria-label="Blue virus particles" style="background:radial-gradient(circle at 55% 45%,#5fb4d9,#1c5f8c 60%,#0d3454)"></div>
  <h3>Stabilize various viruses</h3>
  <p>However judicious and ethic squarely labrad some preparatoy armdil aliqua enim ad minim veniam quis.</p>
  <span class="more">READMORE</span>
</article>
<article class="abs card" style="left:436px">
  <div class="photo" role="img" aria-label="Researcher looking into a microscope" style="background:linear-gradient(120deg,#cfe6ef,#e9f1f3 50%,#a9c7d2)"></div>
  <h3>Viral Vectors</h3>
  <p>However judicious and ethic squarely labrad some preparatoy armdil aliqua enim ad minim veniam quis.</p>
  <span class="more">READMORE</span>
</article>
<article class="abs card" style="left:769px">
  <div class="photo" role="img" aria-label="Syringe and vaccine vial" style="background:linear-gradient(120deg,#f1f3f4,#dfe3e5 55%,#c5ccd0)"></div>
  <h3>Vaccines</h3>
  <p>However judicious and ethic squarely labrad some preparatoy armdil aliqua enim ad minim veniam quis.</p>
  <span class="more">READMORE</span>
</article>

<div class="abs about">
  <h2>About antigen preservation bureau<br><b>Special Care</b> &amp; <b>Attention</b> they need</h2>
  <p>About psyco this however woodpecker krew heedlessly contagiously and much under then bat iguanodon about divisive hello ducked good-ness wow far one circa much devious one excepting far bore speechlessly much ipsum dolor sit amet, consectetur adipiscing elit sed do eiusmod tempor incididunt labore et dolore.</p>
</div>

<!-- applications -->
<div class="abs kicker" style="left:0;top:1773px">Sample Dummy text</div>
<h2 class="abs section-title" style="left:0;top:1814px">Our Applications</h2>

<div class="abs app" style="left:100px;background:var(--gold)">
  <svg width="52" height="52" viewBox="0 0 52 52" fill="none" stroke="#fff" stroke-width="2.5"><rect x="8" y="16" width="36" height="28"/><line x1="8" y1="24" x2="44" y2="24"/><rect x="16" y="6" width="20" height="10"/><line x1="26" y1="29" x2="26" y2="39"/><line x1="21" y1="34" x2="31" y2="34"/></svg>
  <h4>Pharmaceutical</h4><span>readmore</span>
</div>
<div class="abs app" style="left:443px;background:var(--teal)">
  <svg width="52" height="52" viewBox="0 0 52 52" fill="none" stroke="#fff" stroke-width="2.5"><path d="M20 6h12M22 6v14L10 42a4 4 0 0 0 4 5h24a4 4 0 0 0 4-5L30 20V6"/><circle cx="22" cy="36" r="2.5"/><circle cx="31" cy="32" r="2"/></svg>
  <h4>Therapeutic</h4><span>readmore</span>
</div>
<div class="abs app" style="left:789px;background:var(--grey-box)">
  <svg width="52" height="52" viewBox="0 0 52 52" fill="none" stroke="#fff" stroke-width="2.5"><path d="M34 8l10 10M39 13l-21 21-6-6 21-21M12 28l-6 6 6 6M15 37l-9 9M22 22l4 4M27 17l4 4"/></svg>
  <h4>Vaccination</h4><span>readmore</span>
</div>

<!-- articles & reviews -->
<section class="abs light"></section>
<div class="abs col-kicker" style="left:95px;top:2194px">For Better Welness &amp; Hope</div>
<h2 class="abs col-title" style="left:95px;top:2234px">Recent Articles</h2>
<div class="abs col-kicker" style="left:612px;top:2194px">For Better Welness &amp; Hope</div>
<h2 class="abs col-title" style="left:612px;top:2234px">Client Reviews</h2>

<article class="abs article" style="top:2323px">
  <div class="thumb" role="img" aria-label="Blue virus particles" style="background:radial-gradient(circle at 40% 50%,#6fbde0,#174e78 65%,#0b2840)"></div>
  <div><time>Posted: Sep 29, 2018</time><p>One wow wherever a that past reined bitterly racco became canny hypn tically you because ...</p></div>
</article>
<article class="abs article" style="top:2482px">
  <div class="thumb" role="img" aria-label="Pink virus particle" style="background:radial-gradient(circle at 50% 50%,#e0577a,#b03a5a 45%,#4b8db0 80%)"></div>
  <div><time>Posted: Sep 29, 2018</time><p>One wow wherever a that past reined bitterly racco became canny hypn tically you because ...</p></div>
</article>

<div class="abs review">
  <blockquote>Medical prissy so smiling a before contans kerously much notwit ahstan dingt hungry towards dear as darn more cavalier hatche pending rid boa yet more across caterpillar unwound terier crud misread less this globefish positively drank.</blockquote>
  <h5>Elena Morrow</h5>
  <small>Portland, USA</small>
</div>
<div class="abs arrow" style="left:969px;background:#fff;border:1px solid #ddd">
  <svg width="10" height="12" viewBox="0 0 10 12"><path d="M7 1L2 6l5 5" fill="none" stroke="#666" stroke-width="2"/></svg>
</div>
<div class="abs arrow" style="left:1017px;background:#f0a070">
  <svg width="10" height="12" viewBox="0 0 10 12"><path d="M3 1l5 5-5 5" fill="none" stroke="#fff" stroke-width="2"/></svg>
</div>

<!-- map & contact -->
<section class="abs map" role="img" aria-label="Grey street map of the city around the office"></section>
<div class="abs contact-box">
  <h3>Contact Info</h3>
  <ul>
    <li><svg width="16" height="16" viewBox="0 0 16 16"><path d="M8 1a5 5 0 0 0-5 5c0 4 5 9 5 9s5-5 5-9a5 5 0 0 0-5-5z" fill="#fff"/><circle cx="8" cy="6" r="2" fill="var(--gold)"/></svg><span>4120 Harlow Lane, Fairbridge<br>California - 90210</span></li>
    <li><svg width="16" height="14" viewBox="0 0 16 14"><rect x="1" y="2" width="14" height="10" rx="1" fill="#fff"/><path d="M1 3l7 5 7-5" fill="none" stroke="var(--gold)" stroke-width="1.5"/></svg><span>help@apb-lab.example</span></li>
    <li><svg width="16" height="16" viewBox="0 0 16 16"><path d="M3 1h3l1.5 4-2 1.5a9 9 0 0 0 4 4L11 8.5l4 1.5v3a2 2 0 0 1-2 2A12 12 0 0 1 1 3a2 2 0 0 1 2-2z" fill="#fff"/></svg><span>1-435-555-0192</span></li>
  </ul>
</div>
<div class="abs stripe"></div>

<!-- footer -->
<footer class="abs footer">
  <div class="abs" style="left:87px;top:64px;display:flex;align-items:center;gap:8px"><span style="width:30px;height:30px;border-radius:50%;background:#666;display:block"></span><span style="font-size:14px;font-weight:700;color:#ccc">APB</span></div>
  <p class="abs f-text" style="left:87px;top:130px;width:230px">Vestibulum ante ipsum primis in faucis orci luctus et ultrices posuere Vestibulum ante ipsum primisVestibulum ante ipsum primis in faucis orci luctus et ultrices</p>
  <div class="abs f-head" style="left:87px;top:254px">SUBSCRIBE US</div>

  <div class="abs f-head" style="left:351px;top:72px">RECENT TWEETS</div>
  <div class="abs" style="left:351px;top:126px;width:220px">
    <div class="tweet"><i></i><p class="f-text">@Vestibulum ante ipsum primis in faucis orci luctus et ultrices posuere Vestibulum ante ipsum</p></div>
    <div class="tweet"><i></i><p class="f-text">@Vestibulum ante ipsum primis in faucis orci luctus et ultrices posuere Vestibulum ante ipsum</p></div>
    <div class="tweet"><i></i><p class="f-text">@Vestibulum ante ipsum primis in faucis orci luctus et ultrices posuere Vestibulum ante ipsum</p></div>
  </div>

  <div class="abs f-head" style="left:612px;top:72px">QUICK LINK</div>
  <ul class="abs links" style="left:612px;top:120px"><li>Home</li><li>offerings</li><li>products</li><li>services</li><li>contact</li><li>about</li></ul>
  <ul class="abs links" style="left:732px;top:120px"><li>About Us</li><li>Promotions</li><li>Contact Us</li></ul>

  <div class="abs f-head" style="left:876px;top:72px">INSTAGRAM</div>
  <div class="abs insta" style="left:876px;top:135px"></div>
  <div class="abs insta" style="left:955px;top:135px"></div>
  <div class="abs insta" style="left:1033px;top:135px"></div>
  <div class="abs insta" style="left:876px;top:214px"></div>
  <div class="abs insta" style="left:955px;top:214px"></div>
  <div class="abs insta" style="left:1033px;top:214px"></div>
</footer>
<div class="abs subscribe">Email subscribe<b><svg width="14" height="14" viewBox="0 0 14 14"><path d="M1 7l12-6-4 12-2-5z" fill="#fff"/></svg></b></div>

<div class="abs bottom">
  <div class="abs socials"><i></i><i></i><i></i><i></i></div>
  <div class="abs copy">Copyright © 2018 www.apb-lab.example</div>
</div>

</body>
</html>
```